Birchwood Forage Business Cards

I need a business card with my logo, number, Facebook account, and some information about what I am selling. Green card with logo on the front. 847-302-1596 phone number, @birchwoodforage Facebook, •Orchardgrass Hay •Alfalfa Hay •Mixed Grass Hay , and “Premium Quality Hay” all written on the back.

Target Market(s)

Hay

Contact Information for Business Card

Phone number, Facebook, different types of hay.

Colors
00AB8E
00BBA5
67D7C9
C6EFE9
E9F9F6

```html
<!DOCTYPE html>
<html lang="en">
<head>
<meta charset="utf-8">
<title>Birchwood Forage Business Cards</title>
<link href="https://fonts.googleapis.com/css2?family=Source+Sans+3:wght@400&display=swap" rel="stylesheet">
<style>
  :root {
    --green-deep: #00AB8E;
    --green: #00BBA5;
    --green-mid: #67D7C9;
    --green-pale: #C6EFE9;
    --green-mist: #E9F9F6;
    --paper: #F6FAF9;
    --ink-light: #FFFFFF;
  }
  * { margin: 0; padding: 0; box-sizing: border-box; }
  html, body {
    width: 1200px;
    height: 1200px;
    overflow: hidden;
  }
  body {
    background: var(--green-pale);
    font-family: "Source Sans 3", "Myriad Pro", sans-serif;
    font-weight: 400;
    position: relative;
  }
  .card {
    position: absolute;
    left: 180px;
    width: 840px;
    height: 480px;
    border-radius: 4px;
    box-shadow: 0 18px 40px rgba(0, 90, 75, 0.18);
    overflow: hidden;
  }
  .card--front {
    top: 90px;
    background: var(--paper);
    display: flex;
    align-items: center;
    justify-content: center;
  }
  .brand {
    display: flex;
    align-items: center;
    gap: 22px;
  }
  .brand__mark {
    width: 56px;
    height: 56px;
    border: 6px solid var(--green);
  }
  .brand__name {
    color: var(--green);
    font-size: 46px;
    letter-spacing: 0.5px;
  }
  .card--back {
    top: 630px;
    background: var(--green);
    color: var(--ink-light);
  }
  .contact {
    position: absolute;
    left: 230px;
    top: 62px;
  }
  .contact__phone {
    font-size: 46px;
    line-height: 1.05;
    letter-spacing: 1px;
  }
  .contact__handle {
    font-size: 42px;
    line-height: 1.1;
  }
  .contact__rule {
    width: 62px;
    height: 2px;
    background: var(--ink-light);
    margin: 26px 0 22px;
  }
  .products {
    list-style: none;
    font-size: 17px;
    line-height: 1.45;
  }
  .products li::before {
    content: "";
    display: inline-block;
    width: 7px;
    height: 7px;
    border-radius: 50%;
    background: var(--ink-light);
    margin: 0 14px 2px -22px;
    vertical-align: middle;
  }
  .products { padding-left: 22px; }
  .tagline {
    font-size: 27px;
    margin-top: 8px;
  }
  .divider {
    position: absolute;
    left: 520px;
    top: 240px;
    width: 2px;
    height: 200px;
    background: var(--ink-light);
  }
</style>
</head>
<body>
  <section class="card card--front">
    <div class="brand">
      <span class="brand__mark"></span>
      <span class="brand__name">Birchwood Forage</span>
    </div>
  </section>

  <section class="card card--back">
    <div class="contact">
      <p class="contact__phone">847-302-1596</p>
      <p class="contact__handle">@birchwoodforage</p>
      <div class="contact__rule"></div>
      <ul class="products">
        <li>Orchardgrass Hay</li>
        <li>Alfalfa Hay</li>
        <li>Mixed Grass Hay</li>
      </ul>
      <p class="tagline">Premium Quality Hay</p>
    </div>
    <div class="divider"></div>
  </section>
</body>
</html>
```